Agricultural Consulting Website

Provide a modern yet business like website for my new Agriculture Consulting Business in Australia called FenTrove. Whilst we are based in Australia we are targetting both domestic and international markets (especially in Asia). We are targetting corporate, small business, government and farmer clients. The design should compliment our logo also sourced through pixel guild. The webiste should be easy for me to keep updated on a regular basis without the need to go back to the designer.

Industry/Entity Type

Business

Requirements
Must have
• clean crisp feel
• be modern yet business like
• be able to be updated by myself easily

```html
<!DOCTYPE html>
<html lang="en">
<head>
<meta charset="utf-8">
<title>FenTrove – Agricultural Consulting</title>
<link rel="stylesheet" href="https://fonts.googleapis.com/css2?family=Hind:wght@300;400;500;600&family=Open+Sans:wght@400;600;700&display=swap">
<style>
  :root {
    --green: #5c9a0a;
    --green-dark: #4e8606;
    --brown: #663300;
    --brown-dark: #5a2c00;
    --ink: #2a2a2a;
    --white: #ffffff;
    --line: #d9d9d9;
    --sky: #6d8fb8;
    --wheat: #b79a55;
  }
  * { box-sizing: border-box; margin: 0; padding: 0; }
  html, body { width: 1042px; height: 1200px; overflow: hidden; background: var(--white); }
  body { position: relative; font-family: "Open Sans", sans-serif; color: var(--ink); }
  .abs { position: absolute; }

  .top-band { left: 0; top: 0; width: 1042px; height: 14px; background: var(--green); }

  .brand { left: 86px; top: 18px; display: flex; align-items: center; gap: 8px; }
  .brand-mark { width: 52px; height: 56px; background: var(--brown); }
  .brand-name { font-family: "Hind", sans-serif; font-weight: 500; font-size: 42px; color: var(--green); line-height: 1; }

  .main-nav { left: 354px; top: 38px; display: flex; gap: 29px; font-family: "Hind", sans-serif; font-weight: 500; font-size: 15px; color: var(--brown); }
  .main-nav a { color: inherit; text-decoration: none; padding: 2px 1px 3px; }
  .main-nav a.active { color: var(--green); border-top: 2px solid var(--green); border-bottom: 2px solid var(--green); padding: 1px 1px 1px; }

  .search { left: 810px; top: 38px; width: 144px; height: 24px; border: 1px solid var(--brown); display: flex; }
  .search span { flex: 1; font-size: 11px; color: #555; padding: 5px 6px; }
  .search b { width: 27px; background: var(--brown); display: flex; align-items: center; justify-content: center; }

  .hero-panel { left: 86px; top: 85px; width: 228px; height: 396px; background: var(--green); }
  .hero-text { left: 123px; top: 138px; width: 170px; font-family: "Hind", sans-serif; font-weight: 300; font-size: 19px; line-height: 24px; color: var(--white); }
  .hero-cta { left: 123px; top: 301px; width: 143px; height: 35px; background: var(--brown); color: var(--white); font-family: "Hind", sans-serif; font-weight: 400; font-size: 18px; display: flex; align-items: center; justify-content: center; }
  .hero-more { left: 123px; top: 347px; font-size: 12px; color: var(--white); }
  .call { left: 86px; top: 400px; width: 228px; height: 81px; background: var(--brown); }
  .call-edge { left: 86px; top: 396px; }
  .call-label { left: 123px; top: 418px; font-family: "Hind", sans-serif; font-weight: 600; font-size: 12.5px; color: var(--white); display: flex; gap: 6px; align-items: center; }
  .call-number { left: 123px; top: 434px; font-family: "Open Sans", sans-serif; font-weight: 700; font-size: 20px; color: var(--white); }
  .hero-photo { left: 314px; top: 85px; width: 640px; height: 396px; background: linear-gradient(180deg, #5f82b4 0%, #8aa6c9 45%, #b9a064 62%, #9c8444 100%); }
  .slider-btn { top: 253px; width: 30px; height: 30px; border-radius: 50%; background: rgba(255,255,255,.55); display: flex; align-items: center; justify-content: center; }

  .section-title { left: 267px; top: 518px; width: 509px; display: flex; align-items: center; }
  .section-title .rule { flex: 1; height: 1px; background: var(--green); }
  .section-title .dot { width: 14px; height: 14px; border-radius: 50%; background: var(--green); }
  .section-title h2 { font-family: "Hind", sans-serif; font-weight: 400; font-size: 24px; color: var(--green); padding: 0 30px; line-height: 32px; }

  .card { top: 580px; width: 213px; height: 214px; border: 1px solid var(--line); background: var(--white); box-shadow: 0 10px 12px -8px rgba(0,0,0,.15); }
  .card h3 { position: absolute; left: 0; top: 14px; width: 100%; text-align: center; font-family: "Hind", sans-serif; font-weight: 400; font-size: 19px; color: var(--ink); }
  .card .card-photo { position: absolute; left: 15px; top: 46px; width: 182px; height: 83px; }
  .card p { position: absolute; left: 18px; top: 140px; width: 135px; font-size: 11px; line-height: 13px; color: #111; }
  .card .plus { position: absolute; left: 161px; top: 141px; width: 36px; height: 36px; display: flex; align-items: center; justify-content: center; }
  .plus.brown { background: var(--brown); }
  .plus.green { background: var(--green); }

  .about { left: 86px; top: 837px; width: 432px; height: 241px; background: var(--brown); box-shadow: 0 10px 14px -8px rgba(0,0,0,.2); }
  .about h2 { position: absolute; left: 32px; top: 27px; font-family: "Hind", sans-serif; font-weight: 400; font-size: 20px; color: var(--white); }
  .about hr { position: absolute; left: 32px; top: 61px; width: 375px; border: 0; border-top: 1px solid rgba(255,255,255,.7); }
  .about p { position: absolute; left: 32px; top: 71px; width: 378px; font-size: 12.4px; line-height: 16.3px; color: var(--white); }
  .about .more { position: absolute; left: 316px; top: 202px; width: 94px; height: 22px; background: var(--white); color: var(--brown); font-size: 11.5px; font-weight: 600; display: flex; align-items: center; justify-content: center; gap: 3px; }

  .contact-map { left: 524px; top: 837px; width: 430px; height: 241px; background: linear-gradient(160deg, #efe9dc 0%, #e9e3d2 55%, #a8c6ea 80%, #9fbfe6 100%); box-shadow: 0 10px 14px -8px rgba(0,0,0,.2); }
  .contact-tab { left: 524px; top: 837px; }
  .contact-tab-label { left: 541px; top: 844px; font-family: "Hind", sans-serif; font-weight: 600; font-size: 17px; color: var(--white); }
  .map-pin { left: 715px; top: 882px; }

  .footer { left: 0; top: 1126px; width: 1042px; height: 74px; background: var(--green); }
  .footer-links { left: 85px; top: 1147px; font-size: 11px; color: var(--white); display: flex; gap: 13px; }
  .footer-copy { left: 85px; top: 1163px; font-size: 11px; color: var(--white); }
  .social { left: 832px; top: 1148px; display: flex; gap: 14px; }
  .social span { width: 32px; height: 32px; border-radius: 50%; background: var(--white); }
</style>
</head>
<body>
  <div class="abs top-band"></div>

  <header>
    <div class="abs brand">
      <span class="brand-mark"></span>
      <span class="brand-name">FenTrove</span>
    </div>
    <nav class="abs main-nav">
      <a href="#">Home</a>
      <a href="#" class="active">About us</a>
      <a href="#">Services</a>
      <a href="#">Contact</a>
      <a href="#">FAQ’s</a>
      <a href="#">Blog</a>
    </nav>
    <div class="abs search">
      <span>Search</span>
      <b><svg width="11" height="11" viewBox="0 0 12 12"><circle cx="5" cy="5" r="3.5" fill="none" stroke="#fff" stroke-width="1.8"/><line x1="7.5" y1="7.5" x2="11" y2="11" stroke="#fff" stroke-width="2"/></svg></b>
    </div>
  </header>

  <section class="hero">
    <div class="abs hero-panel"></div>
    <p class="abs hero-text">Lorem ipsum dolor sit amet, conse ctetur ad ipiscing elit. In fermentum dolor non augue pretium.</p>
    <div class="abs hero-cta">Get in Touch</div>
    <div class="abs hero-more">Learn More &gt;&gt;</div>
    <div class="abs call"></div>
    <svg class="abs call-edge" width="228" height="6" viewBox="0 0 228 6">
      <path d="M0 6 L0 3 L3 0 L6 3 L9 0 L12 3 L15 0 L18 3 L21 0 L24 3 L27 0 L30 3 L33 0 L36 3 L39 0 L42 3 L45 0 L48 3 L51 0 L54 3 L57 0 L60 3 L63 0 L66 3 L69 0 L72 3 L75 0 L78 3 L81 0 L84 3 L87 0 L90 3 L93 0 L96 3 L99 0 L102 3 L105 0 L108 3 L111 0 L114 3 L117 0 L120 3 L123 0 L126 3 L129 0 L132 3 L135 0 L138 3 L141 0 L144 3 L147 0 L150 3 L153 0 L156 3 L159 0 L162 3 L165 0 L168 3 L171 0 L174 3 L177 0 L180 3 L183 0 L186 3 L189 0 L192 3 L195 0 L198 3 L201 0 L204 3 L207 0 L210 3 L213 0 L216 3 L219 0 L222 3 L225 0 L228 3 L228 6 Z" fill="#663300"/>
    </svg>
    <div class="abs call-label">CALL FOR QUERY
      <svg width="9" height="11" viewBox="0 0 10 12"><path d="M2 1 L4 1 L5 3.5 L3.6 4.6 C4.2 6.4 5 7.4 6.4 8.2 L7.6 7 L10 8.2 L9.6 10.5 C5 11 1 6 1.2 2 Z" fill="#fff"/></svg>
    </div>
    <div class="abs call-number">1800 555 014</div>
    <div class="abs hero-photo" role="img" aria-label="Agronomist in a white coat holding a clipboard and inspecting wheat in a field under blue sky"></div>
    <div class="abs slider-btn" style="left:864px"><svg width="10" height="12" viewBox="0 0 10 12"><path d="M7 1 L2 6 L7 11" fill="none" stroke="#777" stroke-width="2.2"/></svg></div>
    <div class="abs slider-btn" style="left:905px"><svg width="10" height="12" viewBox="0 0 10 12"><path d="M3 1 L8 6 L3 11" fill="none" stroke="#777" stroke-width="2.2"/></svg></div>
  </section>

  <div class="abs section-title">
    <span class="rule"></span><span class="dot"></span>
    <h2>Lorem Text Heading</h2>
    <span class="dot"></span><span class="rule"></span>
  </div>

  <section class="clients">
    <article class="abs card" style="left:86px">
      <h3>Corporate Business</h3>
      <div class="card-photo" role="img" aria-label="Two businessmen with a laptop in green hill country" style="background:linear-gradient(180deg,#8fb3d9 0%,#9bb07a 45%,#6c8a3c 100%)"></div>
      <p>Lorem ipsum dolor sit amet, consec tetur adipis cing elit.In ferme ntum dolor non augue</p>
      <span class="plus brown"><svg width="18" height="18" viewBox="0 0 18 18"><path d="M9 1V17M1 9H17" stroke="#fff" stroke-width="1.6"/></svg></span>
    </article>
    <article class="abs card" style="left:304px">
      <h3>Small Business</h3>
      <div class="card-photo" role="img" aria-label="Cupped hands holding soil with a young seedling" style="background:radial-gradient(circle at 45% 55%,#d9b8a0 0%,#a9c46a 45%,#5e8f22 100%)"></div>
      <p>Lorem ipsum dolor sit amet, consec tetur adipis cing elit.In ferme ntum dolor non augue</p>
      <span class="plus green"><svg width="18" height="18" viewBox="0 0 18 18"><path d="M9 1V17M1 9H17" stroke="#fff" stroke-width="1.6"/></svg></span>
    </article>
    <article class="abs card" style="left:524px">
      <h3>Government</h3>
      <div class="card-photo" role="img" aria-label="Farmer with a tablet in a green crop field" style="background:linear-gradient(180deg,#b8c6d2 0%,#8ea76a 40%,#6d8c3a 100%)"></div>
      <p>Lorem ipsum dolor sit amet, consec tetur adipis cing elit.In ferme ntum dolor non augue</p>
      <span class="plus green"><svg width="18" height="18" viewBox="0 0 18 18"><path d="M9 1V17M1 9H17" stroke="#fff" stroke-width="1.6"/></svg></span>
    </article>
    <article class="abs card" style="left:743px">
      <h3>Farmer Clients</h3>
      <div class="card-photo" role="img" aria-label="Grower checking tall leafy crop plants" style="background:linear-gradient(180deg,#7fa33a 0%,#b7c43c 50%,#3f5e1c 100%)"></div>
      <p>Lorem ipsum dolor sit amet, consec tetur adipis cing elit.In ferme ntum dolor non augue</p>
      <span class="plus green"><svg width="18" height="18" viewBox="0 0 18 18"><path d="M9 1V17M1 9H17" stroke="#fff" stroke-width="1.6"/></svg></span>
    </article>
  </section>

  <section class="abs about">
    <h2>About Us</h2>
    <hr>
    <p>Lorem ipsum dolor sit amet, consectetur adipiscing elit. In fermentum dolor non augue pretium egestas. Donec sem eros, tincidunt at congue ut, posuere sit amet est. Vivamus scelerisque viverra odio sit amet laoreet. Ut nec neque non justo rutrum tempor lobortis eu ante. Aliquam sagittis, nibh quis commodo auctor, risus mauris laoreet lectus, id facilisis libero odio nec enim nibh quis commodo auctor, risus mauris laoreet lectus, id facilisis libero odio nec enim</p>
    <span class="more">Learn More <svg width="9" height="9" viewBox="0 0 9 9"><path d="M4.5 0V9M0 4.5H9" stroke="#663300" stroke-width="2"/></svg></span>
  </section>

  <section class="contact">
    <div class="abs contact-map" role="img" aria-label="Street map of the city area around the office location"></div>
    <svg class="abs contact-tab" width="131" height="37" viewBox="0 0 131 37"><path d="M0 0H131L117 37H0Z" fill="#000"/></svg>
    <div class="abs contact-tab-label">Contact Us</div>
    <svg class="abs map-pin" width="42" height="66" viewBox="0 0 42 66">
      <path d="M21 1C10 1 1 10 1 21C1 34 21 56 21 56C21 56 41 34 41 21C41 10 32 1 21 1Z" fill="#663300" stroke="#3a1d00" stroke-width="1"/>
      <circle cx="21" cy="20" r="8" fill="#fff"/>
      <circle cx="21" cy="61" r="4" fill="#111"/>
    </svg>
  </section>

  <footer>
    <div class="abs footer"></div>
    <nav class="abs footer-links">
      <span>Home</span><span>|</span><span>About us</span><span>|</span><span>Services</span><span>|</span><span>Contact</span><span>|</span><span>FAQ’s</span><span>|</span><span>Blog</span>
    </nav>
    <div class="abs footer-copy">© copyright 2013 with FenTrove &nbsp; | &nbsp; Privacy Policy</div>
    <div class="abs social" aria-label="Social links"><span></span><span></span><span></span></div>
  </footer>
</body>
</html>
```